Für ein Ebook mit dem Titel 'Lichtung - Atemzug für das Herz' mit dem Autorennamen Corinna Wendel benötige ich ein ansprechendes Cover.
Es sollte nicht zu bunt sein. Eher sinnlich und beruhigend. Erdtöne

```html
<!DOCTYPE html>
<html lang="de">
<head>
<meta charset="utf-8">
<title>Lichtung – Atemzug für das Herz</title>
<link rel="stylesheet" href="https://fonts.googleapis.com/css2?family=Roboto+Slab:wght@200;300&display=swap">
<style>
  :root {
    --paper: #f2e9e1;
    --bark: #5c5149;
    --sand: #cdb8a1;
    --ink: #5c5149;
  }
  html, body {
    margin: 0;
    padding: 0;
    width: 752px;
    height: 1200px;
    overflow: hidden;
    background: var(--paper);
  }
  .cover {
    position: relative;
    width: 752px;
    height: 1200px;
    overflow: hidden;
    background: var(--paper);
    font-family: "Roboto Slab", Georgia, serif;
    color: var(--ink);
  }
  .shapes {
    position: absolute;
    inset: 0;
    width: 752px;
    height: 1200px;
  }
  .shape-sand { fill: var(--sand); }
  .shape-bark { fill: var(--bark); }
  .title { margin: 0; font-weight: 200; }
  .line {
    position: absolute;
    left: 0;
    width: 100%;
    margin: 0;
    text-align: center;
    line-height: 1;
    white-space: nowrap;
  }
  .title-line {
    font-size: 78px;
    font-weight: 200;
  }
  .title-main { top: 336px; }
  .title-dash { top: 418px; }
  .title-sub-1 { top: 550px; }
  .title-sub-2 { top: 658px; }
  .author {
    top: 822px;
    font-size: 52px;
    font-weight: 300;
  }
</style>
</head>
<body>
<main class="cover">
  <svg class="shapes" viewBox="0 0 752 1200" xmlns="http://www.w3.org/2000/svg">
    <defs>
      <linearGradient id="branch-tone" x1="0" y1="0" x2="1" y2="1">
        <stop offset="0" stop-color="#cdb8a1" stop-opacity="0.95"/>
        <stop offset="1" stop-color="#cdb8a1" stop-opacity="0.6"/>
      </linearGradient>
    </defs>
    <!-- upper corner: soft pebble and wave -->
    <path class="shape-sand" d="M0,150 C70,128 150,150 172,215 C192,275 150,320 165,375 C178,425 140,470 80,468 C45,466 18,452 0,440 Z"/>
    <path class="shape-bark" d="M0,0 L430,0 C420,90 370,190 290,220 C225,244 175,215 140,178 C105,140 55,128 0,140 Z"/>
    <!-- lower corner: rising hill -->
    <path class="shape-bark" d="M752,760 L752,1200 L410,1200 C405,1120 450,1040 540,990 C620,945 690,900 752,760 Z"/>
    <ellipse class="branch-area" role="img" aria-label="Zweig mit Blättern in Sandtönen"
             cx="650" cy="1005" rx="72" ry="215" transform="rotate(-22 650 1005)"
             fill="url(#branch-tone)"/>
  </svg>

  <h1 class="title">
    <span class="line title-line title-main">Lichtung</span>
    <span class="line title-line title-dash">–</span>
    <span class="line title-line title-sub-1">Atemzug für das</span>
    <span class="line title-line title-sub-2">Herz</span>
  </h1>
  <p class="line author">Corinna Wendel</p>
</main>
</body>
</html>
```